Business card for massage therapy company called Brook Fern Wellness

Need business card for massage therapy company called Brook Fern Wellness. Would like my logo on the front and the back of the card I have 3 options of logos and you can play with what looks better.

Would like this information displayed on the back of the card:

Marcus Ellery
Licensed Massage Therapist
321-555-0147
brookfern-example.com
brookfern_rest_

```html
<!DOCTYPE html>
<html lang="en">
<head>
<meta charset="utf-8">
<title>Brook Fern Wellness — Business Card</title>
<link rel="stylesheet" href="https://fonts.googleapis.com/css2?family=PT+Sans:wght@400;700&display=swap">
<style>
  :root {
    --sage: #737760;
    --ink: #333333;
    --muted: #3d3d3d;
    --paper: #ffffff;
    --backdrop: #ececed;
    --backdrop-edge: #f5f5f5;
  }
  * { box-sizing: border-box; margin: 0; padding: 0; }
  html, body {
    width: 1144px;
    height: 1200px;
    overflow: hidden;
  }
  body {
    position: relative;
    font-family: "PT Sans", sans-serif;
    background: radial-gradient(ellipse at 45% 45%, var(--backdrop) 0%, var(--backdrop-edge) 85%);
    color: var(--ink);
  }

  /* Back of card: contact details */
  .card-back-details {
    position: absolute;
    left: 154px;
    top: 136px;
  }
  .person-name {
    margin-left: 23px;
    font-size: 47px;
    font-weight: 700;
    line-height: 1;
    color: var(--ink);
    letter-spacing: 0.2px;
  }
  .person-title {
    margin-left: 24px;
    margin-top: 6px;
    font-size: 20.5px;
    font-weight: 400;
    color: var(--muted);
    letter-spacing: 0.6px;
  }
  .contact-list {
    list-style: none;
    margin-top: 60px;
  }
  .contact-item {
    display: flex;
    align-items: center;
    height: 24px;
    font-size: 20px;
    color: var(--muted);
    letter-spacing: 0.3px;
  }
  .contact-item + .contact-item { margin-top: 20px; }
  .contact-item:last-child { margin-top: 24px; }
  .contact-icon {
    width: 16px;
    height: 16px;
    margin-right: 7px;
    flex: none;
  }

  /* Back of card: brand panel */
  .brand-panel {
    position: absolute;
    left: 517px;
    top: 59px;
    width: 505px;
    height: 533px;
    background: var(--sage);
  }
  .brand-panel svg { display: block; }

  /* Front of card */
  .card-front {
    position: absolute;
    left: 109px;
    top: 624px;
    width: 913px;
    height: 533px;
    background: var(--paper);
    box-shadow: 0 0 40px rgba(0,0,0,0.04);
    overflow: hidden;
  }
  .front-name {
    position: absolute;
    left: 0;
    right: 0;
    top: 150px;
    text-align: center;
    font-size: 92px;
    line-height: 1.02;
    font-weight: 400;
    color: var(--sage);
    letter-spacing: 1.5px;
  }
  .front-name span { display: block; }
  .front-footer {
    position: absolute;
    left: 0;
    right: 0;
    top: 441px;
    height: 14px;
  }
  .footer-rule {
    position: absolute;
    top: 2px;
    height: 10px;
    background: var(--sage);
  }
  .footer-rule--left { left: 0; width: 292px; border-radius: 0 5px 5px 0; }
  .footer-rule--right { left: 624px; width: 289px; border-radius: 5px 0 0 5px; }
  .footer-web {
    position: absolute;
    left: 332px;
    top: -5px;
    display: flex;
    align-items: center;
    font-size: 20px;
    color: var(--muted);
    letter-spacing: 0.3px;
  }
  .footer-web .contact-icon { width: 15px; height: 15px; }
</style>
</head>
<body>

  <section class="card-back-details">
    <h1 class="person-name">Marcus Ellery</h1>
    <p class="person-title">Licensed Massage Therapist</p>
    <ul class="contact-list">
      <li class="contact-item">
        <svg class="contact-icon" viewBox="0 0 16 16" aria-hidden="true">
          <path fill="#737760" d="M3.6 1.2l2.2 2.4c.4.4.4 1 .1 1.4L4.8 6.3c.9 2 2.5 3.6 4.5 4.6l1.3-1.2c.4-.4 1-.4 1.4 0l2.4 2.2c.4.4.4 1 0 1.4l-1.3 1.2c-.6.5-1.4.7-2.1.4C6.3 13.2 2.8 9.7 1.1 5.1.8 4.4 1 3.6 1.5 3L2.2 1.2c.4-.4 1-.4 1.4 0z"/>
        </svg>
        321-555-0147
      </li>
      <li class="contact-item">
        <svg class="contact-icon" viewBox="0 0 16 16" aria-hidden="true">
          <circle cx="8" cy="8" r="6.5" fill="none" stroke="#737760" stroke-width="1.6"/>
        </svg>
        brookfern_rest_
      </li>
      <li class="contact-item">
        <svg class="contact-icon" viewBox="0 0 16 16" aria-hidden="true">
          <g fill="none" stroke="#737760" stroke-width="1.3">
            <circle cx="8" cy="8" r="6.8"/>
            <ellipse cx="8" cy="8" rx="3" ry="6.8"/>
            <line x1="1.2" y1="8" x2="14.8" y2="8"/>
            <line x1="2.2" y1="4.6" x2="13.8" y2="4.6"/>
            <line x1="2.2" y1="11.4" x2="13.8" y2="11.4"/>
          </g>
        </svg>
        brookfern-example.com
      </li>
    </ul>
  </section>

  <section class="brand-panel" aria-label="Brook Fern Wellness">
    <svg width="505" height="533" viewBox="0 0 505 533">
      <circle cx="277" cy="267" r="160" fill="none" stroke="#ffffff" stroke-width="3.5"/>
      <text x="277" y="256" text-anchor="middle" font-family="PT Sans, sans-serif" font-size="52" fill="#ffffff" letter-spacing="1">Brook Fern</text>
      <text x="277" y="314" text-anchor="middle" font-family="PT Sans, sans-serif" font-size="52" fill="#ffffff" letter-spacing="1">Wellness</text>
    </svg>
  </section>

  <section class="card-front">
    <p class="front-name"><span>Brook Fern</span><span>Wellness</span></p>
    <div class="front-footer">
      <span class="footer-rule footer-rule--left"></span>
      <span class="footer-web">
        <svg class="contact-icon" viewBox="0 0 16 16" aria-hidden="true">
          <g fill="none" stroke="#737760" stroke-width="1.3">
            <circle cx="8" cy="8" r="6.8"/>
            <ellipse cx="8" cy="8" rx="3" ry="6.8"/>
            <line x1="1.2" y1="8" x2="14.8" y2="8"/>
            <line x1="2.2" y1="4.6" x2="13.8" y2="4.6"/>
            <line x1="2.2" y1="11.4" x2="13.8" y2="11.4"/>
          </g>
        </svg>
        brookfern-example.com
      </span>
      <span class="footer-rule footer-rule--right"></span>
    </div>
  </section>

</body>
</html>
```